ROLLFAST FITNESSRoll Out, A UNIQUE CONCIERGE MOBILE SERVICE LAUNCHING in SOUTH FLORIDA

I AM LOOKING TO ATTRACT LEADS FOR CONVERSION WHILE BRINGING OUR SERVICE TO LIFE IN THERE HANDS. WE SERVICE A VERY HIGHLY AFFLUENT CROWD. I would like those on a 5 x 7 two sided card

Target Market(s)

AFFLUENT

Industry/Entity Type

HEALTH AND FITNESS

Font styles to use
Other font styles liked:
• POPINS MED

Colors
0054AA
0677BA
7BADD7
CADEEF
E8F1F8
FFF300
FFF600
FEFA6F
FFFEC7
FFFEE8

Requirements
Must have
• space for postage I INCLUDED CONTENT
Nice to have
• CLASSY FUN LOOK
Should not have
• DULLNESs

```html
<!DOCTYPE html>
<html lang="en">
<head>
<meta charset="utf-8">
<title>SkyBend Fitness – Two-Sided Card</title>
<link href="https://fonts.googleapis.com/css2?family=Oswald:wght@500;700&family=Poppins:wght@500;600;700;800&family=Arvo:wght@400;700&display=swap" rel="stylesheet">
<style>
  :root{
    --yellow:#fff300;
    --yellow-soft:#fefa6f;
    --cyan:#5ccbd9;
    --charcoal:#3b4043;
    --charcoal-deep:#2b2f31;
    --ink:#141414;
    --white:#ffffff;
    --paper:#e9e9e7;
  }
  *{margin:0;padding:0;box-sizing:border-box}
  html,body{width:1200px;height:840px;overflow:hidden;background:#cfd2d4}
  .card-spread{position:relative;width:1200px;height:840px;display:flex}
  .side{position:relative;height:840px;overflow:hidden}
  .side--front{width:598px;background:var(--charcoal-deep)}
  .side--back{width:602px;background:var(--charcoal)}
  .abs{position:absolute}

  /* front */
  .hazard-band{left:0;top:0;width:598px;height:52px;background:var(--yellow)}
  .hazard-band__strip{position:absolute;left:0;top:10px;width:598px;height:30px;background:var(--ink);transform:rotate(1.8deg);transform-origin:left;display:flex;justify-content:space-around;align-items:center}
  .hazard-band__name{font:700 13px/1 'Poppins',sans-serif;color:var(--cyan);letter-spacing:1px}
  .photo-fill{display:block}
  .slogan{font-family:'Oswald',sans-serif;font-weight:700;font-style:italic;color:var(--white);line-height:1;letter-spacing:-1px;white-space:nowrap;transform-origin:left top}
  .slogan--lead{left:50px;top:410px;font-size:50px;transform:scaleX(.83)}
  .slogan--big{left:97px;top:465px;font-size:82px;transform:scaleX(.8)}
  .slogan--big .hl{color:var(--yellow-soft)}
  .slogan--end{left:84px;top:548px;font-size:54px;transform:scaleX(.81)}
  .slogan--end .hl{color:var(--yellow)}
  .brand-name{font-family:'Poppins',sans-serif;font-weight:700;color:var(--cyan);white-space:nowrap;line-height:1}
  .brand-name--front{left:91px;top:624px;font-size:38px}
  .hashtags{left:106px;top:700px;font:700 italic 19px/1 'Oswald',sans-serif;color:var(--yellow);white-space:nowrap}
  .hashtags .alt{color:var(--white);margin-left:8px}
  .front-url{left:188px;top:800px;font:400 16px/1 'Arvo',serif;color:#333;letter-spacing:1.5px}

  /* back */
  .headline{font-family:'Oswald',sans-serif;font-weight:700;font-style:italic;color:var(--white);line-height:1;white-space:nowrap;letter-spacing:-1px;transform-origin:left top}
  .headline--one{left:167px;top:336px;font-size:42px;transform:scaleX(.89)}
  .headline--two{left:191px;top:374px;font-size:64px;transform:scaleX(.87)}
  .headline--three{left:126px;top:436px;font-size:52px;transform:scaleX(.84)}
  .headline--three .hl{color:var(--yellow)}
  .rule{background:var(--yellow);height:3px}
  .brand-name--back{left:150px;top:512px;width:330px;text-align:center;font-size:34px}
  .benefit-frame{left:124px;top:574px;width:380px;height:86px;border-top:2px solid var(--yellow);border-right:2px solid var(--yellow);border-bottom:2px solid var(--yellow)}
  .benefits{left:110px;top:580px;width:380px;text-align:center;font:600 26px/1.02 'Poppins',sans-serif;color:var(--white);letter-spacing:-.5px}
  .covered{left:136px;top:636px;width:340px;height:42px;background:var(--white);font:700 25px/42px 'Poppins',sans-serif;color:var(--ink);text-align:center;letter-spacing:-1px}
  .get-started{left:0;top:690px;width:602px;text-align:center;font:400 19px/1 'Arvo',serif;color:var(--white);letter-spacing:1px}
  .offer-bar{left:76px;top:714px;width:462px;height:32px;background:var(--yellow);font:800 17px/32px 'Poppins',sans-serif;color:var(--ink);text-align:center;letter-spacing:1.2px}
  .visit{left:0;top:750px;width:602px;text-align:center;font:400 16px/1 'Arvo',serif;color:var(--white);letter-spacing:1.3px}
  .visit .go{color:var(--yellow)}
  .contact{top:786px;display:flex;align-items:center;gap:12px;font:700 21px/1 'Arvo',serif;letter-spacing:.5px}
  .contact--phone{left:86px;color:var(--white)}
  .contact--mail{left:288px;color:var(--yellow)}
</style>
</head>
<body>
<main class="card-spread">

  <section class="side side--front">
    <svg class="abs photo-fill" style="left:0;top:0" width="598" height="840" role="img" aria-label="Faded photo of people training beside the fitness truck">
      <defs>
        <linearGradient id="frontShade" x1="0" y1="0" x2="1" y2="1">
          <stop offset="0" stop-color="#34383a"/><stop offset="1" stop-color="#23272a"/>
        </linearGradient>
      </defs>
      <rect width="598" height="840" fill="url(#frontShade)"/>
    </svg>
    <svg class="abs" style="left:0;top:0" width="598" height="420" role="img" aria-label="Photo of the branded pickup truck with training straps on a rooftop">
      <defs>
        <linearGradient id="truckPhoto" x1="0" y1="0" x2="1" y2="1">
          <stop offset="0" stop-color="#f3ef9a"/><stop offset=".45" stop-color="#a9aaa4"/><stop offset="1" stop-color="#66696b"/>
        </linearGradient>
      </defs>
      <path d="M0 0H598V412L560 404 520 396 470 398 430 390 380 384 345 376 300 382 260 368 210 364 170 358 130 348 80 334 40 328 0 322Z" fill="url(#truckPhoto)"/>
      <path d="M0 322L40 328 80 334 130 348 170 358 210 364 260 368 300 382 345 376 380 384 430 390 470 398 520 396 560 404 598 412" fill="none" stroke="#fff300" stroke-width="5"/>
    </svg>
    <div class="abs hazard-band">
      <div class="hazard-band__strip">
        <span class="hazard-band__name">SKYBEND FITNESS</span>
        <span class="hazard-band__name">SKYBEND FITNESS</span>
        <span class="hazard-band__name">SKYBEND FITNESS</span>
      </div>
    </div>

    <div class="abs slogan slogan--lead">“GET FIT ON YOUR</div>
    <div class="abs slogan slogan--big">SCHE<span class="hl">DULE</span></div>
    <div class="abs slogan slogan--end"><span class="hl">ANYWHERE,</span> ANYTIME”</div>
    <svg class="abs" style="left:384px;top:452px" width="214" height="92" role="img" aria-label="Line drawing of the fitness truck"><rect width="214" height="92" fill="none"/></svg>

    <div class="abs brand-name brand-name--front">SKYBEND FITNESS</div>
    <div class="abs hashtags">#HEALTH AND FITNESS<span class="alt">#CONCIERGE FITNESS</span></div>

    <svg class="abs" style="left:0;top:748px" width="598" height="92" role="img" aria-label="Torn paper strip">
      <path d="M0 60L60 44 120 40 180 30 240 26 300 20 360 22 420 6 470 14 480 92 0 92Z" fill="#e9e9e7"/>
    </svg>
    <div class="abs front-url">www.skybendfitness.com</div>
  </section>

  <section class="side side--back">
    <svg class="abs" style="left:0;top:0" width="602" height="350" role="img" aria-label="Black and white photo of clients doing strap workouts at the truck">
      <defs>
        <linearGradient id="groupPhoto" x1="0" y1="0" x2="1" y2="1">
          <stop offset="0" stop-color="#d9d9d9"/><stop offset=".5" stop-color="#8d8d8d"/><stop offset="1" stop-color="#4a4a4a"/>
        </linearGradient>
      </defs>
      <path d="M0 0H602V346L560 336 520 320 480 318 430 314 400 300 360 296 320 286 270 286 230 274 190 272 150 266 100 270 60 260 20 262 0 258Z" fill="url(#groupPhoto)"/>
      <path d="M0 258L20 262 60 260 100 270 150 266 190 272 230 274 270 286 320 286 360 296 400 300 430 314 480 318 520 320 560 336 602 346" fill="none" stroke="#ffffff" stroke-width="5"/>
    </svg>

    <svg class="abs" style="left:6px;top:364px" width="150" height="80" role="img" aria-label="Line drawing of the fitness truck"><rect width="150" height="80" fill="none"/></svg>

    <div class="abs headline headline--one">TRANSFORM</div>
    <div class="abs headline headline--two">YOUR BODY,</div>
    <div class="abs rule" style="left:0;top:461px;width:112px"></div>
    <div class="abs rule" style="left:532px;top:459px;width:70px"></div>
    <div class="abs headline headline--three"><span class="hl">MIND AND</span> SPIRIT&nbsp; WITH</div>
    <div class="abs brand-name brand-name--back">SKYBEND FITNESS</div>

    <div class="abs benefit-frame"></div>
    <div class="abs rule" style="left:484px;top:658px;width:20px;height:2px"></div>
    <div class="abs benefits">Overall Health, Flexibility<br>Agility, Strength,</div>
    <div class="abs covered">WE’VE GOT YOU COVERED</div>

    <div class="abs get-started">Get Started with SkyBend Fitness Today</div>
    <div class="abs offer-bar">FOR FREE CONSULTAION AND ASSESMENT</div>
    <div class="abs visit"><span class="go">go to</span> www.skybendfitness.com</div>

    <div class="abs contact contact--phone">
      <svg width="28" height="28" viewBox="0 0 24 24" aria-hidden="true"><path d="M6.6 3.5l2.3 3.6-1.6 2.2c.9 2.4 2.9 4.6 5.4 5.6l2.2-1.5 3.6 2.3-.9 3c-7.4.2-13.8-6.5-13.9-13.9z" fill="none" stroke="#fff" stroke-width="1.5" stroke-linejoin="round"/><path d="M14 3.5a7 7 0 016.5 6.5M14 6.5a4 4 0 013.5 3.5" fill="none" stroke="#fff" stroke-width="1.4"/></svg>
      <span>720 555 0143</span>
    </div>
    <div class="abs contact contact--mail">
      <svg width="30" height="28" viewBox="0 0 30 28" aria-hidden="true"><path d="M2 11L15 2l13 9v15H2z M2 11l13 9 13-9" fill="none" stroke="#fff300" stroke-width="1.8" stroke-linejoin="round"/><circle cx="15" cy="10" r="3" fill="none" stroke="#fff300" stroke-width="1.5"/></svg>
      <span>info@trailmovefit.com</span>
    </div>
  </section>

</main>
</body>
</html>
```